Corporate Design für Malermeister
Super Arbeit von dem ersten Entwurf an. Schnelle und präzise Umstzung von Änderungen. Durch tolle Vorschläge des Designers sowie meiner Vorstellung ist ein für mich perfektes und stimmiges Corparate Design entstanden. Die Zusammenarbeit war rundum ein voller Erfolg! Sehr zu empfehlen! Auch hier noch mal Danke für deine präzise und schnelle Arbeit. Mann merkt, dass hier mit einem Profi gearbeitet wird!
Zielgruppe
Ich bin Malermeister ,
wir bieten komplettrenovierungen an vom Gestalten der Oberflächen, kreative Wandgestaltung Trockenbau, Bodenverlegearbeiten Parkett, Laminat, Teppich, designböden etc.
Fokus liegt bei den Malerarbeiten! Auch Fassaden werden restaurariert und gestaltet
Wir wollen modern und hochwertig rüber kommen
Aufgabenstellung
Das Logo soll zeigen, dass wir ein moderner kreativer Betrieb sind
da wir eine Diesntaleistung anbieten sollte es auch auf Vertrauen asutrahlen

```html
<!DOCTYPE html>
<html lang="de">
<head>
<meta charset="utf-8">
<title>KlarWand – Corporate Design</title>
<link href="https://fonts.googleapis.com/css2?family=Open+Sans:wght@300;400;600;700&family=Roboto+Condensed:wght@400;700&display=swap" rel="stylesheet">
<style>
:root{
  --blue:#1b6db4;
  --grey:#555759;
  --text:#3f4043;
  --label:#8a8c8f;
  --board:#f8f8f8;
  --paper:#ffffff;
  --faint:#ededed;
}
*{margin:0;padding:0;box-sizing:border-box}
html,body{width:1200px;height:3000px;overflow:hidden}
body{background:var(--paper);font-family:"Open Sans",sans-serif;color:var(--text);position:relative}
.board{position:absolute;left:0;top:0;width:1200px;height:2293px;background:var(--board)}
.section-label{position:absolute;left:0;width:1200px;text-align:center;font-weight:300;font-size:18px;color:var(--label);letter-spacing:.5px}

/* lockup: dot hangs left of the name so text edges align */
.lockup{position:absolute;white-space:nowrap}
.lockup .name{font-family:"Roboto Condensed",sans-serif;font-weight:700;color:var(--blue);display:flex;align-items:center;line-height:1;margin-left:-.5em}
.lockup .name .dot{display:inline-block;background:var(--blue);margin-right:.18em;width:.32em;height:.32em}
.lockup .trade{font-family:"Roboto Condensed",sans-serif;font-weight:700;color:var(--grey);line-height:1;letter-spacing:.02em}
.lockup .claim{font-weight:300;color:var(--text);line-height:1}

/* cards */
.card{position:absolute;background:var(--paper);box-shadow:0 1px 5px rgba(0,0,0,.22)}
.contact{position:absolute;font-size:18px;line-height:27px;white-space:nowrap}
.contact .person{color:var(--blue);font-weight:600;font-size:20px;line-height:24px}
.contact .role{font-size:17px;line-height:21px}
.contact .web{color:var(--blue);font-weight:700}
.icon{position:absolute;fill:var(--blue)}
.services{position:absolute;font-size:17.5px;line-height:20.6px;white-space:nowrap}
.services h3{color:var(--blue);font-weight:600;font-size:20px;line-height:22px}
.services ul{list-style:none}
.services li{position:relative}
.services li::before{content:"";position:absolute;left:-21px;top:9px;width:3px;height:3px;border-radius:50%;background:var(--blue)}
.services .group+.group{margin-top:24px}

/* letterhead */
.sheet{position:absolute;width:551px;height:777px;background:var(--paper);box-shadow:0 1px 5px rgba(0,0,0,.22);overflow:hidden}
.fold{position:absolute;left:0;top:275px;width:14px;height:1px;background:#9a9a9a}
.sender{position:absolute;left:64px;top:139px;font-size:6.5px;color:var(--text);white-space:nowrap}
.sheet-contact{position:absolute;left:390px;top:160px;font-size:8px;line-height:12px;white-space:nowrap}
.sheet-contact .person{color:var(--blue);font-weight:700;font-size:9px;line-height:10px}
.sheet-contact .web{color:var(--blue);font-weight:700}
.sheet-contact .gap{height:8px}
.watermark{position:absolute;left:22px;top:380px;width:484px;text-align:center;font-family:"Roboto Condensed",sans-serif;font-weight:700;font-size:128px;color:var(--faint);line-height:1}
.footer-col{position:absolute;top:708px;height:69px;border-left:2px solid var(--blue);padding:4px 0 0 5px;font-size:6.5px;line-height:8.5px;white-space:nowrap}
.footer-col .web{color:var(--blue)}
.footer-col .sp{height:6px}

/* vehicle livery, shown flat */
.livery{position:absolute;left:0;top:2293px;width:1200px;height:707px;background:var(--paper)}
</style>
</head>
<body>
<div class="board">
  <p class="section-label" style="top:92px">LOGO</p>

  <div class="lockup" style="left:509px;top:370px">
    <div class="name" style="font-size:82px"><span class="dot"></span>KlarWand</div>
    <div class="trade" style="font-size:31px;margin-top:8px">MALERMEISTERBETRIEB</div>
    <div class="claim" style="font-size:23px;margin-top:9px">Gutes bewahren | Räume gestalten</div>
  </div>

  <p class="section-label" style="top:584px">VISITENKARTE S.1 + S.2</p>

  <!-- business card front -->
  <div class="card" style="left:119px;top:664px;width:401px;height:621px">
    <div class="lockup" style="left:142px;top:176px">
      <div class="name" style="font-size:61px"><span class="dot"></span>KlarWand</div>
      <div class="trade" style="font-size:23px;margin-top:6px">MALERMEISTERBETRIEB</div>
      <div class="claim" style="font-size:16px;margin-top:8px">Gutes bewahren | Räume gestalten</div>
    </div>
    <div class="contact" style="left:142px;top:320px">
      <div class="person">Jonas Keller</div>
      <div class="role">Malermeister</div>
    </div>
    <svg class="icon" style="left:113px;top:385px" width="20" height="18" viewBox="0 0 20 18"><path d="M10 1 1 9h3v8h5v-5h2v5h5V9h3z"/></svg>
    <div class="contact" style="left:142px;top:381px">Birkenallee 12<br>59821 Talheim</div>
    <svg class="icon" style="left:117px;top:462px" width="12" height="19" viewBox="0 0 12 19"><path d="M2 0h8a2 2 0 0 1 2 2v15a2 2 0 0 1-2 2H2a2 2 0 0 1-2-2V2a2 2 0 0 1 2-2zm0 3v12h8V3z"/></svg>
    <div class="contact" style="left:142px;top:457px">0170 - 214 36 58</div>
    <svg class="icon" style="left:112px;top:518px" width="22" height="15" viewBox="0 0 22 15"><path d="M0 0h22v2L11 9 0 2zm0 4 11 7 11-7v11H0z"/></svg>
    <svg class="icon" style="left:114px;top:543px" width="19" height="19" viewBox="0 0 19 19"><circle cx="9.5" cy="9.5" r="9" fill="none" stroke="#1b6db4" stroke-width="2"/><path d="M4 6c2 0 3 1 3 3s2 2 2 4-1 3 0 4l-4-1-2-5zM11 3c2 1 1 3 3 3l2 3-2 3-2-1-1-3z"/></svg>
    <div class="contact" style="left:142px;top:512px">maler@klarwand.de<br><span class="web">www.klarwand.de</span></div>
  </div>

  <!-- business card back -->
  <div class="card" style="left:686px;top:664px;width:400px;height:615px">
    <div class="lockup" style="left:142px;top:174px">
      <div class="name" style="font-size:61px"><span class="dot"></span>KlarWand</div>
      <div class="trade" style="font-size:23px;margin-top:6px">MALERMEISTERBETRIEB</div>
      <div class="claim" style="font-size:16px;margin-top:8px">Gutes bewahren | Räume gestalten</div>
    </div>
    <div class="services" style="left:141px;top:316px">
      <div class="group">
        <h3>Malerarbeiten</h3>
        <ul><li>Malen &amp; Tapezieren</li><li>Gestalten von Oberflächen</li><li>kreative Wandgestaltung</li><li>Fassadengestaltung</li><li>Restaurierung</li></ul>
      </div>
      <div class="group">
        <h3>Innenarbeiten</h3>
        <ul><li>Teppich</li><li>Laminat</li><li>Parkett</li><li>Designerböden</li><li>Trockenbau</li></ul>
      </div>
    </div>
  </div>

  <p class="section-label" style="top:1336px">BRIEFPAPIER S.1 + S.2</p>

  <!-- letterhead page 1 -->
  <div class="sheet" style="left:36px;top:1410px">
    <div class="watermark">KlarWand</div>
    <div class="lockup" style="left:376px;top:94px">
      <div class="name" style="font-size:32px"><span class="dot"></span>KlarWand</div>
      <div class="trade" style="font-size:12px;margin-top:3px">MALERMEISTERBETRIEB</div>
      <div class="claim" style="font-size:7.8px;margin-top:4px">Gutes bewahren | Räume gestalten</div>
    </div>
    <div class="sender">KlarWand &nbsp;|&nbsp; Birkenallee 12 &nbsp;|&nbsp; 59821 Talheim</div>
    <div class="sheet-contact">
      <div class="person">Jonas Keller</div>
      <div>Malermeister</div>
      <div class="gap"></div>
      <div>Birkenallee 12<br>59821 Talheim</div>
      <div class="gap"></div>
      <div>0170 - 214 36 58<br>maler@klarwand.de<br><span class="web">www.klarwand.de</span></div>
    </div>
    <svg class="icon" style="left:377px;top:189px" width="9" height="8" viewBox="0 0 20 18"><path d="M10 1 1 9h3v8h5v-5h2v5h5V9h3z"/></svg>
    <svg class="icon" style="left:379px;top:225px" width="5" height="8" viewBox="0 0 12 19"><path d="M2 0h8a2 2 0 0 1 2 2v15a2 2 0 0 1-2 2H2a2 2 0 0 1-2-2V2a2 2 0 0 1 2-2zm0 3v12h8V3z"/></svg>
    <svg class="icon" style="left:377px;top:238px" width="9" height="6" viewBox="0 0 22 15"><path d="M0 0h22v2L11 9 0 2zm0 4 11 7 11-7v11H0z"/></svg>
    <svg class="icon" style="left:377px;top:249px" width="8" height="8" viewBox="0 0 19 19"><circle cx="9.5" cy="9.5" r="9"/></svg>
    <div class="fold"></div>
    <div class="footer-col" style="left:38px">KlarWand<div class="sp"></div>Jonas Keller<br>Birkenallee 12<br>59821 Talheim</div>
    <div class="footer-col" style="left:195px">Kontakt:<div class="sp"></div>0170 - 214 36 58<br>maler@klarwand.de<br><span class="web">www.klarwand.de</span></div>
    <div class="footer-col" style="left:357px">Kreisbank Talheim<br>IBAN: DE12 3456 0000 1234 5678 90<br>BIC: KRBTDE00XXX<br>Finanzamt Talheim<br>Steuernummer: 3012345 6789</div>
  </div>

  <!-- letterhead page 2 -->
  <div class="sheet" style="left:610px;top:1410px">
    <div class="watermark">KlarWand</div>
    <div class="lockup" style="left:377px;top:94px">
      <div class="name" style="font-size:32px"><span class="dot"></span>KlarWand</div>
      <div class="trade" style="font-size:12px;margin-top:3px">MALERMEISTERBETRIEB</div>
      <div class="claim" style="font-size:7.8px;margin-top:4px">Gutes bewahren | Räume gestalten</div>
    </div>
    <div class="fold"></div>
    <div class="footer-col" style="left:38px">KlarWand<div class="sp"></div>Jonas Keller<br>Birkenallee 12<br>59821 Talheim</div>
    <div class="footer-col" style="left:195px">Kontakt:<div class="sp"></div>0170 - 214 36 58<br>maler@klarwand.de<br><span class="web">www.klarwand.de</span></div>
    <div class="footer-col" style="left:357px">Kreisbank Talheim<br>IBAN: DE12 3456 0000 1234 5678 90<br>BIC: KRBTDE00XXX<br>Finanzamt Talheim<br>Steuernummer: 3012345 6789</div>
  </div>
</div>

<!-- vehicle livery -->
<div class="livery">
  <div class="lockup" style="left:836px;top:268px">
    <div class="name" style="font-size:66px"><span class="dot"></span>KlarWand</div>
    <div class="trade" style="font-size:29px;margin-top:10px">MALERMEISTERBETRIEB</div>
    <div class="claim" style="font-size:24px;margin-top:12px;margin-left:-71px">Gutes bewahren | Räume gestalten</div>
  </div>
</div>
</body>
</html>
```